Car finance company business card

Create a nice business card for our car financing company , Visit our website www.birchlanefinance.com for the phone number and idea of the company look. Please do not be afraid to be creative. Name on card Is Marc-Antoine Beaulieu and phone number is on our website adress of business is
27816 Boulevard Saint-Orvel,
Mirabel, QC K4R 2T8

```html
<!DOCTYPE html>
<html lang="fr">
<head>
<meta charset="UTF-8">
<title>Birch Lane Finance – Carte d'affaires</title>
<link href="https://fonts.googleapis.com/css2?family=Arimo:wght@400;700&family=Montserrat:wght@700;800&display=swap" rel="stylesheet">
<style>
  :root {
    --page: #e9ebee;
    --brand-blue: #1a7fc6;
    --brand-blue-light: #3aa0e4;
    --ink: #111111;
    --white: #ffffff;
    --tick: #f26a21;
    --fox-orange: #f07a24;
    --fox-purple: #5a55c9;
  }
  * { box-sizing: border-box; margin: 0; padding: 0; }
  html, body {
    width: 1200px; height: 905px; overflow: hidden;
    background: var(--page);
    font-family: "Arimo", Arial, sans-serif;
  }
  .card {
    position: absolute; left: 280px;
    width: 640px; height: 366px;
    border-radius: 22px; overflow: hidden;
    box-shadow: 0 8px 24px rgba(0,0,0,.18);
  }
  .card--front { top: 48px; background: var(--brand-blue); color: var(--white); }
  .card--back { top: 490px; background: var(--white); color: var(--ink); }

  /* Front */
  .offer { position: absolute; left: 44px; top: 86px; }
  .offer__headline {
    font-family: "Montserrat", sans-serif; font-weight: 800;
    font-size: 21px; line-height: 1.12; text-transform: uppercase;
    margin-bottom: 12px;
  }
  .offer__list { list-style: none; font-size: 16px; line-height: 1.3; }
  .offer__list li { display: flex; align-items: center; gap: 8px; }
  .offer__list svg { width: 12px; height: 12px; flex: none; }
  .mascot-art {
    position: absolute; right: 36px; top: 40px;
    width: 250px; height: 260px; border-radius: 50%;
    background: radial-gradient(circle at 45% 40%, var(--fox-orange), #d95e14 55%, var(--fox-purple) 100%);
    opacity: .9;
  }

  /* Back */
  .swoosh { position: absolute; inset: 0; width: 100%; height: 100%; }
  .person { position: absolute; right: 40px; top: 30px; text-align: right; }
  .person__name {
    font-family: "Montserrat", sans-serif; font-weight: 700;
    font-size: 18px; color: var(--white); text-transform: uppercase; letter-spacing: .3px;
  }
  .person__title {
    font-family: "Montserrat", sans-serif; font-weight: 700;
    font-size: 13px; color: var(--brand-blue-light); text-transform: uppercase; margin-top: 2px;
  }
  .brand {
    position: absolute; left: 44px; top: 150px;
    display: flex; align-items: center; gap: 12px;
  }
  .brand__dot { width: 38px; height: 38px; border-radius: 50%; background: var(--fox-orange); }
  .brand__name {
    font-family: "Montserrat", sans-serif; font-weight: 800;
    font-size: 30px; color: var(--ink); text-transform: uppercase;
  }
  .contact { position: absolute; left: 44px; bottom: 34px; list-style: none; font-size: 17px; }
  .contact li { display: flex; align-items: center; gap: 12px; margin-top: 6px; }
  .contact__icon {
    width: 26px; height: 26px; border-radius: 5px; background: var(--brand-blue);
    display: flex; align-items: center; justify-content: center;
  }
  .contact__icon svg { width: 16px; height: 16px; }
  .address {
    position: absolute; right: 40px; bottom: 110px;
    text-align: right; font-size: 17px; line-height: 1.3;
  }
</style>
</head>
<body>

<section class="card card--front">
  <div class="offer">
    <h2 class="offer__headline">1re, 2e, 3e<br>chance au crédit<br>aucun cas refusé</h2>
    <ul class="offer__list">
      <li><svg viewBox="0 0 12 12"><path d="M1 6l3 3 7-8" fill="none" stroke="var(--tick)" stroke-width="2.4"/></svg>Proposition au consommateur</li>
      <li><svg viewBox="0 0 12 12"><path d="M1 6l3 3 7-8" fill="none" stroke="var(--tick)" stroke-width="2.4"/></svg>Remise volontaire</li>
      <li><svg viewBox="0 0 12 12"><path d="M1 6l3 3 7-8" fill="none" stroke="var(--tick)" stroke-width="2.4"/></svg>Retards de paiements</li>
      <li><svg viewBox="0 0 12 12"><path d="M1 6l3 3 7-8" fill="none" stroke="var(--tick)" stroke-width="2.4"/></svg>Recouvrements</li>
      <li><svg viewBox="0 0 12 12"><path d="M1 6l3 3 7-8" fill="none" stroke="var(--tick)" stroke-width="2.4"/></svg>Faible revenu</li>
      <li><svg viewBox="0 0 12 12"><path d="M1 6l3 3 7-8" fill="none" stroke="var(--tick)" stroke-width="2.4"/></svg>Récemment travailleur autonome</li>
      <li><svg viewBox="0 0 12 12"><path d="M1 6l3 3 7-8" fill="none" stroke="var(--tick)" stroke-width="2.4"/></svg>Faillite</li>
      <li><svg viewBox="0 0 12 12"><path d="M1 6l3 3 7-8" fill="none" stroke="var(--tick)" stroke-width="2.4"/></svg>mauvais crédit</li>
    </ul>
  </div>
  <div class="mascot-art" role="img" aria-label="Cartoon mascot in a suit holding car keys"></div>
</section>

<section class="card card--back">
  <svg class="swoosh" viewBox="0 0 640 366" preserveAspectRatio="none" aria-hidden="true">
    <path d="M0 0H640V190C560 120 420 95 230 100C150 102 80 108 0 120Z" fill="var(--ink)"/>
    <path d="M230 100C420 95 560 120 640 190V230C570 150 430 115 230 100Z" fill="var(--brand-blue)"/>
  </svg>
  <div class="person">
    <p class="person__name">Marc-Antoine Beaulieu</p>
    <p class="person__title">Managing Director</p>
  </div>
  <div class="brand">
    <span class="brand__dot"></span>
    <span class="brand__name">Birch Lane Finance</span>
  </div>
  <p class="address">27816 Boulevard Saint-Orvel<br>Mirabel, QC K4R 2T8</p>
  <ul class="contact">
    <li><span class="contact__icon"><svg viewBox="0 0 16 16"><path d="M4 2l2 3-1.5 1.5a8 8 0 0 0 5 5L11 10l3 2-1.5 2.5C7 14 2 9 1.5 3.5Z" fill="var(--white)"/></svg></span>(514) 555-0172</li>
    <li><span class="contact__icon"><svg viewBox="0 0 16 16"><rect x="2" y="4" width="12" height="8" fill="none" stroke="var(--white)" stroke-width="1.5"/><path d="M2 4l6 5 6-5" fill="none" stroke="var(--white)" stroke-width="1.5"/></svg></span>marc@birchlanefinance.com</li>
    <li><span class="contact__icon"><svg viewBox="0 0 16 16"><circle cx="8" cy="8" r="6" fill="none" stroke="var(--white)" stroke-width="1.3"/><ellipse cx="8" cy="8" rx="2.6" ry="6" fill="none" stroke="var(--white)" stroke-width="1.2"/><path d="M2 8h12" stroke="var(--white)" stroke-width="1.2"/></svg></span>www.birchlanefinance.com</li>
  </ul>
</section>

</body>
</html>
```